Wordpress website for a new Podcast

Hi, We are looking for a designer to create a wordpress website project for a new podcast and publish it on the domain we own.

The show is called “Bright Gatherings” (logo included) and its aim is to interview guests who work as professional facilitators, trainers, teachers and coaches. The show has a positive vibe, is fun, vibrant and full of positive energy. These are the feelings we want to convey in the design.

The website should have a similar structure to: https://www.corefocusloop.example/ with the following content:

1) The main page including:
- navigation bar and social buttons at the top
- main graphic design featuring the latest episode
- "latest episodes" section displaying 3 episodes (please design a mask to be used for new episodes when they air together with the face of the interviewee) -> this will link to the respective episodes
- please design an "bright gatherings" book cover mockup to be inluded as a banner -> this will link to Bookvale
- subscribe to the newsletter - a banner capturing the name and email of the user -> to be connected to PostFinch.
-> a working episode search.

2) Episodes page
- the show will be divided into seasons (12 episodes each) and each episode will need a separate "blog entry" including:
-> A short article (4-5 paragraphs) + stock image
-> interviewee's bio and social links

3) Meet the hosts page
- including bios of the two hosts of the show
- links to their social profiles
- a "request speaker availability" form which sends an email

Some additional nice-to-haves:
1) Good and clean Bio's would be awesome (both for the hosts & the interviewees),
2) an easily navigable episode system,
3) a keyword/date search option
4) easy to share options (share to ChatNest, Friendlane, Chirpline, CareerMesh) 5) We must be able to track how the podcasts are shared (trackwise metrics?)

```html
<!DOCTYPE html>
<html lang="en">
<head>
<meta charset="utf-8">
<title>Bright Gatherings – Podcast</title>
<link href="https://fonts.googleapis.com/css2?family=PT+Sans:wght@400;700&display=swap" rel="stylesheet">
<style>
:root{
  --brand:#f2340d;
  --brand-warm:#f7a21a;
  --ink:#1c1c1c;
  --muted:#555;
  --white:#fff;
  --footer:#0f0f0f;
  --footer-low:#141414;
  --line:#d6d6d6;
}
*{box-sizing:border-box;margin:0;padding:0}
html,body{width:748px;height:1200px;overflow:hidden;background:var(--white)}
body{font-family:"PT Sans",sans-serif;color:var(--ink)}
.page{position:relative;width:748px;height:1200px}
.abs{position:absolute}

/* header */
.site-header{left:0;top:0;width:748px;height:69px;background:var(--white)}
.brand-box{left:99px;top:0;width:98px;height:98px;background:radial-gradient(circle at 50% 45%,var(--brand-warm),var(--brand) 70%);display:flex;align-items:center;justify-content:center;text-align:center;z-index:3}
.brand-name{color:var(--white);font-weight:700;font-size:14px;line-height:1.05;letter-spacing:.3px}
.social-top{right:156px;top:12px;display:flex;gap:9px;font-size:9.5px;color:var(--ink);white-space:nowrap}
.divider{left:600px;top:11px;width:1px;height:16px;background:var(--line)}
.top-search{left:612px;top:12px;font-size:9px;color:#888;display:flex;align-items:center;gap:3px}
.main-nav{top:40px;left:0;width:748px;font-size:10.5px;color:#444}
.main-nav span{position:absolute}
.main-nav .current{color:var(--ink)}
.nav-underline{left:277px;top:67px;width:32px;height:2px;background:var(--brand)}

/* hero */
.hero{left:0;top:69px;width:748px;height:327px;background:radial-gradient(ellipse at 55% 40%,#5b5b5b,#3a3a3a 55%,#2a2a2a)}
.hero-title{left:90px;top:174px;width:290px;text-align:center;color:var(--white);font-weight:700;font-size:27px;letter-spacing:.2px}
.hero-sub{left:90px;top:209px;width:282px;text-align:center;color:var(--white);font-size:11.5px;line-height:17px}
.btn{background:var(--brand);color:var(--white);font-weight:700;text-align:center;display:flex;align-items:center;justify-content:center}
.hero-btn{left:181px;top:253px;width:101px;height:29px;font-size:11px}
.arrow{width:36px;height:36px;border-radius:50%;background:rgba(160,160,160,.75);top:213px}
.book{left:437px;top:110px;width:138px;height:245px}

/* episodes */
.section-title{left:0;top:432px;width:748px;text-align:center;font-weight:700;font-size:22px}
.section-title em{font-style:normal;color:var(--brand)}
.card{top:484px;width:174px;height:272px;border:1px solid var(--line);background:var(--white)}
.card-photo{left:0;top:0;width:172px;height:123px}
.podcast-mask{left:73px;top:92px;width:26px;height:26px}
.ep-num{left:0;top:135px;width:172px;text-align:center;color:var(--brand);font-size:10.5px}
.ep-title{left:0;top:154px;width:172px;text-align:center;font-size:12.5px;line-height:14.5px;font-weight:400}
.ep-desc{left:12px;top:186px;width:148px;text-align:center;font-size:8px;line-height:10.5px;color:var(--muted)}
.card-btn{left:9px;top:228px;width:156px;height:30px;font-size:11px}

/* newsletter */
.newsletter{left:0;top:805px;width:748px;height:226px;background:linear-gradient(100deg,#eda617 0%,#f06a12 45%,#f2340d 80%)}
.news-title{left:0;top:858px;width:748px;text-align:center;color:var(--white);font-weight:700;font-size:22px}
.news-sub{left:0;top:893px;width:736px;text-align:center;color:var(--white);font-size:11.5px}
.field{top:923px;height:35px;background:var(--white);font-size:10px;color:#555;display:flex;align-items:center;padding-left:13px}
.sub-btn{left:525px;top:923px;width:104px;height:35px;border:1.5px solid var(--white);color:var(--white);font-weight:700;font-size:12px;display:flex;align-items:center;justify-content:center}

/* footer */
.footer-search-band{left:0;top:1031px;width:748px;height:70px;background:var(--footer)}
.footer-band{left:0;top:1101px;width:748px;height:99px;background:var(--footer-low)}
.search-label{left:111px;top:1057px;color:var(--white);font-weight:700;font-size:14px}
.search-box{left:311px;top:1049px;width:334px;height:35px;border:1px solid #777;display:flex;align-items:center;padding-left:12px;gap:5px;color:#666;font-size:10px}
.footer-brand{left:107px;top:1101px;width:75px;height:75px}
.footer-brand .brand-name{font-size:10px}
.footer-nav{top:1122px;left:0;width:748px;color:var(--white);font-size:10.5px}
.footer-nav span{position:absolute}
.copyright{left:213px;top:1144px;color:#aaa;font-size:9px}
.social-foot{left:570px;top:1124px;display:flex;gap:6px;color:var(--white);font-size:8.5px;white-space:nowrap}
</style>
</head>
<body>
<div class="page">

  <header class="site-header abs"></header>
  <div class="brand-box abs"><span class="brand-name">BRIGHT<br>GATHERINGS</span></div>
  <div class="social-top abs"><span>Chirpline</span><span>Friendlane</span><span>CareerMesh</span><span>ChatNest</span></div>
  <div class="divider abs"></div>
  <div class="top-search abs">
    <svg width="10" height="10" viewBox="0 0 10 10"><circle cx="4" cy="4" r="3" fill="none" stroke="#888" stroke-width="1.3"/><line x1="6.2" y1="6.2" x2="9" y2="9" stroke="#888" stroke-width="1.4"/></svg>Search
  </div>
  <nav class="main-nav abs">
    <span class="current" style="left:279px">Home</span>
    <span style="left:334px">Episode</span>
    <span style="left:398px">Meet the Hosts</span>
    <span style="left:494px">Blogs</span>
    <span style="left:548px">Podcasts</span>
    <span style="left:615px">Resources</span>
  </nav>
  <div class="nav-underline abs"></div>

  <section class="hero abs" role="img" aria-label="Dimmed photo of a woman reading a tablet in a café"></section>
  <h1 class="hero-title abs">BRIGHT GATHERINGS</h1>
  <p class="hero-sub abs">Lorem ipsum dolor sit amet consectetuer<br>adipiscing elit Nam cursus Morbi</p>
  <a class="btn hero-btn abs">CLICK HERE</a>
  <div class="arrow abs" style="left:52px"><svg width="36" height="36" viewBox="0 0 36 36"><polyline points="21,11 14,18 21,25" fill="none" stroke="#111" stroke-width="2"/></svg></div>
  <div class="arrow abs" style="left:654px"><svg width="36" height="36" viewBox="0 0 36 36"><polyline points="15,11 22,18 15,25" fill="none" stroke="#111" stroke-width="2"/></svg></div>
  <svg class="book abs" viewBox="0 0 138 245">
    <defs><radialGradient id="cover" cx="45%" cy="45%" r="55%"><stop offset="0" stop-color="#f7a21a"/><stop offset="0.7" stop-color="#f2340d"/></radialGradient></defs>
    <polygon points="124,6 138,8 138,240 124,245" fill="#cfcfcf"/>
    <polygon points="0,14 124,0 124,245 0,231" fill="url(#cover)"/>
    <text x="62" y="88" text-anchor="middle" font-family="PT Sans, sans-serif" font-weight="700" font-size="16" fill="#ffffff">BRIGHT</text>
    <text x="62" y="108" text-anchor="middle" font-family="PT Sans, sans-serif" font-weight="700" font-size="16" fill="#ffffff">GATHERINGS</text>
  </svg>

  <h2 class="section-title abs">LATEST <em>PODCAST EPISODE</em></h2>

  <article class="card abs" style="left:100px">
    <div class="card-photo abs" role="img" aria-label="Guest portrait for the episode" style="background:linear-gradient(160deg,#7d8da3,#c9c4c0)"></div>
    <svg class="podcast-mask abs" viewBox="0 0 26 26" aria-hidden="true"><circle cx="13" cy="11" r="10" fill="none" stroke="#fff" stroke-width="1.8" stroke-dasharray="40 23" transform="rotate(130 13 11)"/><circle cx="13" cy="11" r="6" fill="none" stroke="#fff" stroke-width="1.8" stroke-dasharray="24 14" transform="rotate(130 13 11)"/><circle cx="13" cy="11" r="2.5" fill="#fff"/><rect x="11.6" y="14" width="2.8" height="10" rx="1.4" fill="#fff"/></svg>
    <div class="ep-num abs">Episode 125</div>
    <h3 class="ep-title abs">Lorem ipsum dolor sit<br>amet consectetuer</h3>
    <p class="ep-desc abs">tristique vitae consequat nec porta vel lectus Nulla sit amet diam Duis non nunc Nulla rhoncus dictum</p>
    <a class="btn card-btn abs">EXPLORE</a>
  </article>
  <article class="card abs" style="left:287px">
    <div class="card-photo abs" role="img" aria-label="Guest portrait for the episode" style="background:linear-gradient(160deg,#6c6c6c,#2c2f36)"></div>
    <svg class="podcast-mask abs" viewBox="0 0 26 26" aria-hidden="true"><circle cx="13" cy="11" r="10" fill="none" stroke="#fff" stroke-width="1.8" stroke-dasharray="40 23" transform="rotate(130 13 11)"/><circle cx="13" cy="11" r="6" fill="none" stroke="#fff" stroke-width="1.8" stroke-dasharray="24 14" transform="rotate(130 13 11)"/><circle cx="13" cy="11" r="2.5" fill="#fff"/><rect x="11.6" y="14" width="2.8" height="10" rx="1.4" fill="#fff"/></svg>
    <div class="ep-num abs">Episode 125</div>
    <h3 class="ep-title abs">Lorem ipsum dolor sit<br>amet consectetuer</h3>
    <p class="ep-desc abs">tristique vitae consequat nec porta vel lectus Nulla sit amet diam Duis non nunc Nulla rhoncus dictum</p>
    <a class="btn card-btn abs">EXPLORE</a>
  </article>
  <article class="card abs" style="left:474px">
    <div class="card-photo abs" role="img" aria-label="Guest portrait for the episode" style="background:linear-gradient(160deg,#58656a,#4a5f86)"></div>
    <svg class="podcast-mask abs" viewBox="0 0 26 26" aria-hidden="true"><circle cx="13" cy="11" r="10" fill="none" stroke="#fff" stroke-width="1.8" stroke-dasharray="40 23" transform="rotate(130 13 11)"/><circle cx="13" cy="11" r="6" fill="none" stroke="#fff" stroke-width="1.8" stroke-dasharray="24 14" transform="rotate(130 13 11)"/><circle cx="13" cy="11" r="2.5" fill="#fff"/><rect x="11.6" y="14" width="2.8" height="10" rx="1.4" fill="#fff"/></svg>
    <div class="ep-num abs">Episode 125</div>
    <h3 class="ep-title abs">Lorem ipsum dolor sit<br>amet consectetuer</h3>
    <p class="ep-desc abs">tristique vitae consequat nec porta vel lectus Nulla sit amet diam Duis non nunc Nulla rhoncus dictum</p>
    <a class="btn card-btn abs">EXPLORE</a>
  </article>

  <section class="newsletter abs"></section>
  <h2 class="news-title abs">SUBSCRIBE TO THE NEWSLETTER</h2>
  <p class="news-sub abs">tristique vitae consequat nec porta vel lectus Nulla sit amet</p>
  <div class="field abs" style="left:127px;width:193px">Your Name</div>
  <div class="field abs" style="left:326px;width:193px;padding-left:15px">Email address</div>
  <div class="sub-btn abs">SUBSCRIBE</div>

  <footer>
    <div class="footer-search-band abs"></div>
    <div class="footer-band abs"></div>
    <div class="search-label abs">A WORKING EPISODE SEARCH</div>
    <div class="search-box abs">
      <svg width="14" height="14" viewBox="0 0 14 14"><circle cx="6" cy="6" r="4.5" fill="none" stroke="#666" stroke-width="1.6"/><line x1="9.3" y1="9.3" x2="13" y2="13" stroke="#666" stroke-width="1.8"/></svg>Search here
    </div>
    <div class="brand-box footer-brand abs"><span class="brand-name">BRIGHT<br>GATHERINGS</span></div>
    <nav class="footer-nav abs">
      <span style="left:213px">Home</span>
      <span style="left:260px">Episode</span>
      <span style="left:315px">Meet the Hosts</span>
      <span style="left:403px">Blogs</span>
      <span style="left:448px">Podcasts</span>
      <span style="left:507px">Resources</span>
    </nav>
    <div class="copyright abs">© 2019 Company Name &nbsp;All right reserved</div>
    <div class="social-foot abs"><span>Chirpline</span><span>Friendlane</span><span>CareerMesh</span><span>ChatNest</span></div>
  </footer>

</div>
</body>
</html>
```